International Clinical Software Company needs a new business card design

We are looking for a new business card design for our company that has recently expanded into the UK market, making us a multinational company.
After having rebranded our website and produced a new style guide, we are looking for a business card that is creative and attention grabbing, while being consistent with the style and colour scheme used on the new website, www.brookvale.example
We produce care management technology for the aged care market, but the main aspect we aim to communicate is the human element of our software, and the way it assists in providing better care for aged people, and stronger relationships between aged people and the staff that care for them.
Our current business card is a dark green with gold text, which makes the text quite difficult to read, not very aesthetically appealing and the colour scheme looks quite dated.
We would like something fresh and modern, that can still be colourful but doesn't use large blocks of dark colour, and uses the colours within our logo.
Something tying in with the leaves that are used in our logo could work quite nicely, along with the Autumn/Fall colours of soft greens, yellows and reds (also in our existing logo). However also happy to look at fresh, completely out of the box ideas we may not have yet considered.
Target Market(s)
The people that receive this business card work in the aged card or health industry and are either corporate/management level staff or clinical (Registered Nurses, care workers etc.)
Industry/Entity Type
Health Product
Contact Information for Business Card
Company Name - BrookvaleTech
Company locations: United Kingdom, Australia, New Zealand
Staff Details:
Staff name: Dermot Quill
Staff job title: Executive Chairman
Staff email: d.quill@brookvale.example
Office phone number: 01632 960418
Font styles to use
Other font styles liked:
- Calibri
Requirements
Must have
- Must include the BrookvaleTech brand name in it's current font
- Must include logo (3 leaves in gold circle)
- Must include Business Card Details
Nice to have
- Elements of gold
- White space
- Something autumn themed but not too cliched
Should not have
- No blue - used by a major competitor and we would like to differentiate from them
- Large blocks of dark green colour (the green that appears in our leaves on the logo on our current business card is the background colour and it is far too dark)

```html
<!DOCTYPE html>
<html lang="en">
<head>
<meta charset="utf-8">
<title>BrookvaleTech Business Card</title>
<link href="https://fonts.googleapis.com/css2?family=Open+Sans:ital,wght@0,300;0,400;0,700;1,700&display=swap" rel="stylesheet">
<style>
  :root {
    --page-bg: #b8bdc8;
    --card-bg: #ffffff;
    --olive: #9a9400;
    --leaf-green: #4a6a14;
    --berry: #8f0029;
    --gold: #a89a72;
    --text-green: #4a6519;
  }
  * { margin: 0; padding: 0; box-sizing: border-box; }
  html, body {
    width: 1200px;
    height: 1000px;
    overflow: hidden;
    background: var(--page-bg);
    font-family: "Open Sans", Calibri, Arial, sans-serif;
  }
  .card {
    position: absolute;
    left: 81px;
    top: 170px;
    width: 1050px;
    height: 600px;
    background: var(--card-bg);
    overflow: hidden;
  }
  .card-shapes {
    position: absolute;
    inset: 0;
  }
  .brand {
    position: absolute;
    left: 76px;
    top: 80px;
    display: flex;
    align-items: flex-start;
    gap: 22px;
  }
  .brand-mark {
    width: 100px;
    height: 100px;
    border-radius: 50%;
    background: var(--gold);
    flex-shrink: 0;
  }
  .brand-text { color: var(--gold); font-weight: 300; }
  .brand-name {
    font-size: 42px;
    line-height: 1;
    margin-top: 16px;
    letter-spacing: -0.5px;
  }
  .brand-regions {
    font-size: 23px;
    line-height: 1;
    margin-top: 14px;
    white-space: nowrap;
  }
  .person {
    position: absolute;
    right: 146px;
    top: 305px;
    text-align: right;
  }
  .person-name {
    font-size: 46px;
    font-weight: 700;
    color: var(--text-green);
    line-height: 1.1;
  }
  .person-title {
    font-size: 37px;
    font-weight: 700;
    font-style: italic;
    color: var(--gold);
    line-height: 1.2;
  }
  .contacts {
    position: absolute;
    left: 75px;
    top: 448px;
    list-style: none;
    color: var(--text-green);
    font-size: 28px;
  }
  .contact-item {
    display: flex;
    align-items: center;
    height: 40px;
  }
  .contact-icon {
    width: 32px;
    height: 32px;
    margin-right: 22px;
    fill: var(--text-green);
  }
</style>
</head>
<body>
  <div class="card">
    <svg class="card-shapes" width="1050" height="600" viewBox="0 0 1050 600" aria-hidden="true">
      <polygon points="446,0 1050,0 1050,210 796,122" fill="var(--olive)"/>
      <polygon points="796,122 1050,210 1050,347 965,401" fill="var(--leaf-green)"/>
      <polygon points="1050,347 1050,600 649,600" fill="var(--berry)"/>
    </svg>

    <div class="brand">
      <div class="brand-mark"></div>
      <div class="brand-text">
        <div class="brand-name">BrookvaleTech</div>
        <div class="brand-regions">United Kingdom | Australia | New Zealand</div>
      </div>
    </div>

    <div class="person">
      <div class="person-name">Dermot Quill</div>
      <div class="person-title">Excecutive Chairman</div>
    </div>

    <ul class="contacts">
      <li class="contact-item">
        <svg class="contact-icon" viewBox="0 0 32 32" aria-hidden="true">
          <path d="M1 9h30v15H1z M1 9l15 9 15-9" fill="var(--text-green)" stroke="#fff" stroke-width="1.5"/>
        </svg>
        d.quill@brookvale.example
      </li>
      <li class="contact-item">
        <svg class="contact-icon" viewBox="0 0 32 32" aria-hidden="true">
          <path d="M9 2h14a2 2 0 0 1 2 2v24a2 2 0 0 1-2 2H9a2 2 0 0 1-2-2V4a2 2 0 0 1 2-2zm1 3v18h12V5zm6 20a1.5 1.5 0 1 0 0 3 1.5 1.5 0 0 0 0-3z"/>
        </svg>
        01632 960418
      </li>
    </ul>
  </div>
</body>
</html>
```